redesign of www.varqolo.com

Need redesign of our website to be more professionally looking. International import & export, warehousing and distribution business primarily from China to North America.

A few professional pictures needed on the new website.

Contact form also is needed.

Total 5 - 10 pages will be OK.

```html
<!DOCTYPE html>
<html lang="en">
<head>
<meta charset="utf-8">
<title>Varqolo – Your Gateway to Asia</title>
<link href="https://fonts.googleapis.com/css2?family=PT+Sans+Narrow:wght@400;700&family=Open+Sans:wght@300;400;600&display=swap" rel="stylesheet">
<style>
:root{
  --orange:#f0a018;
  --orange-dark:#e07a10;
  --ink:#2b2b2b;
  --nav:#5f6b78;
  --text:#666;
  --link:#3e5f86;
  --panel:#f1f3f2;
  --footer:#e9e9e9;
  --white:#fff;
}
*{margin:0;padding:0;box-sizing:border-box}
html,body{width:1024px;height:1200px;overflow:hidden}
body{position:relative;background:#eef0ef;font-family:'Open Sans',sans-serif;color:var(--text)}
.abs{position:absolute}

.site-header{left:0;top:0;width:1024px;height:83px;background:var(--white);border-top:3px solid var(--ink)}
.phone-tab{left:602px;top:0;width:290px;height:27px;background:var(--ink);border-radius:0 0 0 14px;color:#fff;font:700 13px 'PT Sans Narrow',sans-serif;display:flex;align-items:center;gap:7px;padding-left:14px}
.phone-tab b{color:var(--orange)}
.brand{left:124px;top:20px;display:flex;align-items:center;gap:10px}
.brand-dot{width:14px;height:14px;border-radius:50%;background:var(--orange)}
.brand-name{font:700 34px 'PT Sans Narrow',sans-serif;color:var(--ink);letter-spacing:.5px}
.main-nav{top:44px;font:700 14px 'PT Sans Narrow',sans-serif;color:var(--nav);letter-spacing:.3px}
.main-nav.active{color:#3a4653}
.contact-btn{left:775px;top:35px;width:111px;height:36px;background:linear-gradient(#f7b733,#ee9412);border-radius:3px;color:#fff;font:700 14px 'PT Sans Narrow',sans-serif;display:flex;align-items:center;justify-content:center;gap:8px}

.hero{left:0;top:83px;width:1024px;height:397px;background:linear-gradient(100deg,#c98a68 0%,#8d6a62 18%,#4a4b55 30%,#c9cbd4 45%,#e7e6ea 60%,#b8b3b9 80%,#6b5c57 100%)}
.hero-shade{left:0;top:300px;width:1024px;height:180px;background:linear-gradient(transparent,rgba(30,22,18,.65))}
.arrow{width:36px;height:36px;border-radius:50%;top:236px;display:flex;align-items:center;justify-content:center;border:3px solid rgba(255,255,255,.35)}
.arrow.prev{left:78px;background:var(--orange)}
.arrow.next{left:904px;background:#333}
.hero-title{left:134px;top:334px;font:700 32px 'PT Sans Narrow',sans-serif;color:#fff;letter-spacing:-.5px}
.hero-copy{left:138px;top:385px;width:752px;font:400 14.5px/17px 'PT Sans Narrow',sans-serif;color:#fff}

.panel{left:108px;top:439px;width:802px;height:560px;background:var(--panel);border-radius:3px;box-shadow:0 10px 40px rgba(0,0,0,.12)}
.product-photo{left:136px;top:478px;width:158px;height:210px;background:linear-gradient(#fafafa,#e4e4e4)}
h2.section-title{font:700 20px 'PT Sans Narrow',sans-serif;color:#2f2f2f}
.body-copy{font:300 9.8px/16px 'Open Sans',sans-serif;color:#666}
.learn-btn{left:311px;top:659px;width:64px;height:28px;border:1px solid #ccc;border-radius:3px;background:linear-gradient(#f7f7f7,#e6e6e6);font:400 9px 'Open Sans',sans-serif;color:#777;display:flex;align-items:center;justify-content:center}

.card{top:719px;width:237px;height:271px;background:#fff;border-top:6px solid var(--orange-dark);box-shadow:0 1px 4px rgba(0,0,0,.15)}
.card h3{position:absolute;top:22px;left:0;width:100%;text-align:center;font:700 18px 'PT Sans Narrow',sans-serif;color:#2f2f2f}
.card-photo{position:absolute;left:18px;top:48px;width:200px;height:104px}
.card p{position:absolute;left:20px;top:174px;width:205px;font:400 11px/15.3px 'Open Sans',sans-serif;color:#666}
.card a{position:absolute;left:20px;top:234px;font:700 12px 'Open Sans',sans-serif;color:var(--link);text-decoration:underline}

.site-footer{left:0;top:1018px;width:1024px;height:146px;background:var(--footer)}
.foot-brand{left:132px;top:1070px;display:flex;align-items:center;gap:8px}
.foot-brand .brand-name{font-size:26px}
.foot-brand .brand-dot{width:11px;height:11px}
.foot-head{font:600 12px 'Open Sans',sans-serif;color:#777;top:1042px}
.foot-list{list-style:none;top:1068px;font:400 8.8px 'Open Sans',sans-serif;color:#888}
.foot-list li{height:19.2px;display:flex;align-items:center;gap:6px}
.foot-list li::before{content:"";border-left:4px solid #999;border-top:3px solid transparent;border-bottom:3px solid transparent}
.foot-list li.current{color:var(--orange-dark)}
.contact-list{left:577px;top:1068px;font:400 8.8px 'Open Sans',sans-serif;color:#888}
.contact-row{position:absolute;left:0;display:flex;gap:12px;align-items:flex-start;white-space:nowrap}
.contact-row svg{width:11px;height:11px;flex:none}
.social{top:1070px;width:27px;height:27px;border-radius:3px}
.bottom-bar{left:0;top:1164px;width:1024px;height:36px;background:var(--orange);font:400 8.8px 'Open Sans',sans-serif;color:#6a4a10}
</style>
</head>
<body>

<header class="abs site-header"></header>
<div class="abs phone-tab">
  <svg width="14" height="14" viewBox="0 0 14 14"><circle cx="7" cy="7" r="6.2" fill="none" stroke="#fff" stroke-width="1.2"/><path d="M4.6 4c.4-.4.8-.3 1 .1l.5 1c.1.3 0 .5-.2.7l-.3.3c.3.8 1 1.5 1.8 1.8l.3-.3c.2-.2.4-.3.7-.2l1 .5c.4.2.5.6.1 1-.6.6-1.5.7-2.3.3C5.8 8.4 5 7.6 4.4 6.3 4 5.5 4 4.6 4.6 4z" fill="#fff"/></svg>
  FOR INQUIRIES, CALL US: <b>1-800-555-01942</b>
</div>
<div class="abs brand"><span class="brand-dot"></span><span class="brand-name">VARQOLO</span></div>
<nav>
  <a class="abs main-nav active" style="left:494px">HOME</a>
  <a class="abs main-nav" style="left:552px">ABOUT US</a>
  <a class="abs main-nav" style="left:631px">SERVICES</a>
  <a class="abs main-nav" style="left:707px">CONTACT</a>
</nav>
<a class="abs contact-btn">
  <svg width="18" height="13" viewBox="0 0 18 13"><rect x="1" y="1" width="16" height="11" fill="none" stroke="#fff" stroke-width="1.5"/><path d="M1 1l8 6 8-6" fill="none" stroke="#fff" stroke-width="1.5"/></svg>
  CONTACT US
</a>

<section>
  <div class="abs hero" role="img" aria-label="Photo of a white semi truck driving on a desert highway at sunset"></div>
  <div class="abs hero-shade"></div>
  <div class="abs arrow prev"><svg width="8" height="8" viewBox="0 0 8 8"><path d="M5.5 1L2.5 4l3 3" fill="none" stroke="#fff" stroke-width="1.5"/></svg></div>
  <div class="abs arrow next"><svg width="8" height="8" viewBox="0 0 8 8"><path d="M2.5 1l3 3-3 3" fill="none" stroke="#fff" stroke-width="1.5"/></svg></div>
  <h1 class="abs hero-title">Your Gateway to Asia</h1>
  <p class="abs hero-copy">We are committed to utilize the MOST COST EFFECTIVE resources to help our clients in product development, prototyping, sampling, manufacturing, arranging custom clearance &amp; shipment delivery to the door in a hassle free environment.</p>
</section>

<main>
  <div class="abs panel"></div>
  <div class="abs product-photo" role="img" aria-label="Photo of assorted door handles, locks and hinges"></div>

  <h2 class="abs section-title" style="left:311px;top:470px">Welcome to Varqolo</h2>
  <p class="abs body-copy" style="left:313px;top:504px;width:295px">It is a long established fact that a reader will be distracted by the readable content of a page when looking at its layout. The point of using Lorem Ipsum is that it has a more-or-less normal distribution of letters, as opposed to using 'Content here, content here', making it look like readable English.</p>
  <p class="abs body-copy" style="left:313px;top:600px;width:295px">Lorem ipsum dolor sit amet, consectetur adipisicing elit, sed do eiusmod tempor incididunt ut labore et dolore magna aliqua. Ut enim ad minim veniam, quis nostrud exercitation ullamco laboris</p>
  <a class="abs learn-btn">Learn More</a>

  <h2 class="abs section-title" style="left:649px;top:470px">Varqolo's Goals</h2>
  <p class="abs body-copy" style="left:647px;top:504px;width:240px">It is a long established fact that a reader will be distracted by the readable content of a page when looking at its layout. The point of using Lorem Ipsum is that it has a more-or-less normal distribution</p>
  <h2 class="abs section-title" style="left:649px;top:590px">Varqolo's Principle</h2>
  <p class="abs body-copy" style="left:647px;top:624px;width:240px">It is a long established fact that a reader will be distracted by the readable content of a page when looking at its layout. The point of using Lorem Ipsum is that it has a more-or-less normal distribution</p>

  <article class="abs card" style="left:133px">
    <h3>IMPORT &amp; EXPORT</h3>
    <div class="card-photo" role="img" aria-label="Photo of a container ship at sea" style="background:linear-gradient(#e3ecf3 0%,#bfd3e3 45%,#5d5a60 60%,#22303f 80%,#3f6a8c 100%)"></div>
    <p>Lorem ipsum dolor sit amet, consectetur adipisicing elit, sed do eiusmod tempor incididunt ut labore .</p>
    <a>READ MORE</a>
  </article>
  <article class="abs card" style="left:390px">
    <h3>WAREHOUSING &amp; DISTRIBUTION</h3>
    <div class="card-photo" role="img" aria-label="Photo of a forklift in a warehouse with stacked boxes" style="background:linear-gradient(#8a7a64 0%,#b59468 40%,#c99a4a 60%,#d9d6d2 100%)"></div>
    <p style="top:172px">Lorem ipsum dolor sit amet, consectetur adipisicing elit, sed do eiusmod tempor incididunt ut labore .</p>
    <a style="top:232px">READ MORE</a>
  </article>
  <article class="abs card" style="left:647px">
    <h3>SOURCING</h3>
    <div class="card-photo" role="img" aria-label="Photo of a business team reviewing documents together" style="background:linear-gradient(90deg,#d8c8b8 0%,#c2a58c 30%,#e9e7e4 60%,#bfc7cc 100%)"></div>
    <p>Lorem ipsum dolor sit amet, consectetur adipisicing elit, sed do eiusmod tempor incididunt ut labore .</p>
    <a>READ MORE</a>
  </article>
</main>

<footer>
  <div class="abs site-footer"></div>
  <div class="abs foot-brand"><span class="brand-dot"></span><span class="brand-name">VARQOLO</span></div>

  <h4 class="abs foot-head" style="left:321px">Navigation</h4>
  <ul class="abs foot-list" style="left:320px">
    <li>Home</li><li>About</li><li>Services</li><li>Contact</li>
  </ul>

  <h4 class="abs foot-head" style="left:448px">Services</h4>
  <ul class="abs foot-list" style="left:448px">
    <li class="current">Service</li><li>Service</li><li>Service</li><li>Service</li>
  </ul>

  <h4 class="abs foot-head" style="left:577px">Contact Us</h4>
  <div class="abs contact-list">
    <div class="contact-row" style="top:1px"><svg viewBox="0 0 11 11"><path d="M2 1c.5-.5 1-.4 1.3.1l.7 1.3c.2.4 0 .7-.3.9l-.4.4c.4 1 1.2 1.9 2.2 2.3l.4-.4c.3-.3.6-.4.9-.2l1.3.7c.5.3.6.8.1 1.3-.8.8-2 .9-3 .4C3.5 7 2.4 5.9 1.6 4.2 1.1 3.1 1.2 1.8 2 1z" fill="#999"/></svg>+1800-555-0194</div>
    <div class="contact-row" style="top:25px"><svg viewBox="0 0 11 11"><rect x="0.5" y="2" width="10" height="7" fill="#999"/><path d="M0.5 2l5 4 5-4" fill="none" stroke="#e9e9e9" stroke-width="1"/></svg>info@yourwebsite.com</div>
    <div class="contact-row" style="top:49px"><svg viewBox="0 0 11 11"><path d="M5.5 0.5a3.5 3.5 0 0 1 3.5 3.5c0 2.5-3.5 6.5-3.5 6.5S2 6.5 2 4a3.5 3.5 0 0 1 3.5-3.5z" fill="#999"/><circle cx="5.5" cy="4" r="1.3" fill="#e9e9e9"/></svg><span style="line-height:18px">Your Address, Your Country<br>Your Zip Code</span></div>
  </div>

  <h4 class="abs foot-head" style="left:750px">Social</h4>
  <span class="abs social" style="left:751px;background:#3b5a94"></span>
  <span class="abs social" style="left:788px;background:#2aa3db"></span>
  <span class="abs social" style="left:825px;background:#1b6fa3"></span>
  <span class="abs social" style="left:862px;background:#d33b2c"></span>

  <div class="abs bottom-bar">
    <span class="abs" style="left:134px;top:12px">Copyright 2014 © Varqolo - All Rights Reserved</span>
    <span class="abs" style="left:778px;top:12px">Site Map &nbsp;&nbsp;•&nbsp;&nbsp; Privacy Policy</span>
  </div>
</footer>

</body>
</html>
```